Modern Billboard Ad for Criminal Defense Firm

10.5 x 36 We're looking for something to set us apart from the local competition. Looking for sleek and modern. We're a mid-sized firm in a small market city. We want to give the artist room to be creative on this one.
Thanks

Target Market(s)

Adult clients who have been charged with a crime/DWI

Industry/Entity Type

legal

Font styles to use
Serif
Sans Serif

Requirements
Must have
• Needs to have the firm name in large lettering. Law Offices of Marcus T Whitfield. “PLLC” does not have to be included. Phone number of (555) 384-1927 should be included but not the main focus.
Nice to have
• A call to action or something similar. “Don’t go it alone, call today.”, “ Arrested?”

```html
<!DOCTYPE html>
<html lang="en">
<head>
<meta charset="utf-8">
<title>Law Offices of Marcus T Whitfield — Billboard</title>
<link href="https://fonts.googleapis.com/css2?family=Montserrat:wght@400;500;600;800&display=swap" rel="stylesheet">
<style>
  :root {
    --navy-deep: #161a33;
    --slate: #2a2f45;
    --royal: #1f6fd1;
    --indigo: #3a3a9e;
    --violet: #4a2a86;
    --plum: #6b3aa0;
    --yellow: #fff200;
    --white: #ffffff;
    --strip: #1b1a48;
  }
  * { margin: 0; padding: 0; box-sizing: border-box; }
  html, body {
    width: 1200px; height: 425px; overflow: hidden;
    background: var(--navy-deep);
    font-family: "Montserrat", sans-serif;
  }
  .billboard {
    position: relative; width: 1200px; height: 425px; overflow: hidden;
  }
  .backdrop { position: absolute; inset: 0; }
  .attorney-photo {
    position: absolute; left: 0; top: 0; width: 330px; height: 425px;
  }
  .award-badge {
    position: absolute; left: 218px; top: 28px; width: 109px; height: 186px;
  }
  .headline {
    position: absolute; left: 340px; top: 58px; width: 820px;
  }
  .firm-intro {
    display: flex; align-items: center; gap: 18px;
  }
  .firm-intro-text {
    color: var(--yellow); font-weight: 500; font-size: 46px;
    letter-spacing: 0.5px; line-height: 1; white-space: nowrap;
  }
  .rule { flex: 1; height: 5px; background: var(--white); }
  .firm-name {
    color: var(--white); font-weight: 800; font-size: 67px;
    line-height: 1; margin-top: 14px; white-space: nowrap;
    letter-spacing: -0.5px;
  }
  .rule-full { height: 5px; background: var(--white); margin-top: 10px; }
  .tagline {
    position: absolute; left: 340px; top: 262px;
    display: flex; align-items: baseline; gap: 18px; white-space: nowrap;
  }
  .tagline-question {
    color: var(--yellow); font-weight: 800; font-size: 62px; line-height: 1;
  }
  .tagline-support {
    color: var(--white); font-weight: 500; font-size: 42px; line-height: 1;
  }
  .call-strip { position: absolute; left: 329px; top: 350px; width: 240px; height: 75px; }
  .call-label {
    position: absolute; left: 340px; top: 366px;
    color: var(--white); font-weight: 600; font-size: 31px; line-height: 1.3;
  }
  .phone {
    position: absolute; left: 566px; top: 355px;
    color: var(--white); font-weight: 500; font-size: 50px; line-height: 1.3;
    letter-spacing: 0.5px;
  }
</style>
</head>
<body>
<main class="billboard">
  <svg class="backdrop" width="1200" height="425" viewBox="0 0 1200 425" role="img" aria-label="City skyline at dusk blending into a close-up of hands in handcuffs">
    <defs>
      <linearGradient id="city" x1="0" y1="0" x2="0" y2="1">
        <stop offset="0" stop-color="#3a3c52"/>
        <stop offset="1" stop-color="#1c1f30"/>
      </linearGradient>
      <linearGradient id="cuffs" x1="0" y1="0" x2="1" y2="1">
        <stop offset="0" stop-color="#1f6fd1"/>
        <stop offset="0.45" stop-color="#3a3a9e"/>
        <stop offset="1" stop-color="#5a2c8e"/>
      </linearGradient>
    </defs>
    <rect width="1200" height="425" fill="url(#city)"/>
    <polygon points="760,0 1200,0 1200,425 590,425" fill="url(#cuffs)"/>
  </svg>

  <svg class="attorney-photo" viewBox="0 0 330 425" role="img" aria-label="Portrait of the attorney in a grey plaid suit and blue tie">
    <defs>
      <linearGradient id="portrait" x1="0" y1="0" x2="0" y2="1">
        <stop offset="0" stop-color="#2b2e40"/>
        <stop offset="0.5" stop-color="#6c6d73"/>
        <stop offset="1" stop-color="#85868a"/>
      </linearGradient>
    </defs>
    <rect width="330" height="425" fill="url(#portrait)"/>
  </svg>

  <svg class="award-badge" viewBox="0 0 109 186" role="img" aria-label="Community choice award badge">
    <rect width="109" height="186" fill="#29a8e0"/>
    <rect x="5" y="5" width="99" height="150" fill="#1d1d1f"/>
  </svg>

  <header class="headline">
    <div class="firm-intro">
      <span class="firm-intro-text">LAW OFFICES OF</span>
      <span class="rule"></span>
    </div>
    <h1 class="firm-name">MARCUS T WHITFIELD</h1>
    <div class="rule-full"></div>
  </header>

  <p class="tagline">
    <span class="tagline-question">ARRESTED?</span>
    <span class="tagline-support">Don’t go it alone,</span>
  </p>

  <svg class="call-strip" viewBox="0 0 240 75" aria-hidden="true">
    <polygon points="0,0 200,0 240,75 0,75" fill="var(--strip)"/>
  </svg>
  <p class="call-label">Call today :</p>
  <p class="phone">(555) 384-1927</p>
</main>
</body>
</html>
```